Original catchy book cover

I need a book cover for my book "The Steady Harbor Manual" (https://quillpress.example/harbormanual). This will be a book self published on brightmart.
The book talks about the following concepts:
- Iterative product delivery
- Early discovery using feedback from customers
- Start small, think big, move fast
- Slice the product into valuable increments that can be validated with customers
- Experimental approach to deciding the next slice of work
A simple cover that stands out from the business books already out there! Some examples are:
https://www.brightmart.example/Field-Notes-Thriving-Teams-Steadily-ebook/dp/Q00XTR4KWZ/ref=sr_1_1?ie=UTF8&qid=1500000001&sr=8-1&keywords=field+notes
https://www.brightmart.example/Quiet-Harbor-Almanac-Shape-Offerings-ebook/dp/Q00MVK219J/ref=sr_1_1?s=digital-text&ie=UTF8&qid=1500000002&sr=1-1&keywords=quiet+harbor+almanac
https://www.brightmart.example/Course-Charts-Renewed-Heading-Fog-ebook/dp/Q099WT71ZD/ref=pd_sim_351_2?_encoding=UTF8&psc=1&refRID=9QZTRWJDDAV52LM0NKPP
Lastly, attached are 2 draft covers that i've been playing with. Would love a graphic as part of the cover if it makes sense in your design! The graphic should tie to the meaning or themes of the book. Emphasis on ways of working, collaboration, experimentation, hypothesis, agile, incremental or adaptive. Those are some words that describe the content of the book.
Alternatively, something abstract could also be an option if a literal graphic doesn't suit the theme of your design.
Target Market(s)
Product owners, scrum masters, people in the agile community, software developers, designers
Industry/Entity Type
Information Technology
Font styles to use
Colors
Designer to choose colors to be used in the design.
Requirements
Must have
- Title, Subtitle, Author Name
- Back of the book should have space for a description (use lorem ipsum for now)
- Please use the editorial logo
- (please omit "created by Tomas Verlindt" because the editorial logo replaces that.
- The design must be original art or graphics (i.e. it should be similar to another cover in this topic).
Nice to have
- A graphic would be ideal if it is relevant to the book topic, otherwise a nice simple cover that uses colors or patterns that are easy to recall.
- The color suggestions below are suggestions only. Do not feel you have to incorporate all the colors and feel free to recommend an alternate palette.
Should not have
- Clipart or generic stock art photos. Images for the sake of images, traditional logos (e.g. a computer, a phone etc unless it's part of an overall theme that ties the logos together).

```html
<!DOCTYPE html>
<html lang="en">
<head>
<meta charset="utf-8">
<title>The Steady Harbor Manual — Cover</title>
<link rel="stylesheet" href="https://fonts.googleapis.com/css2?family=Bebas+Neue&family=Lato:wght@400;700;900&display=swap">
<style>
  :root {
    --stage-bg: #dde5e9;
    --cover-blue: #0099ff;
    --ink-white: #ffffff;
  }
  html, body {
    margin: 0;
    padding: 0;
    width: 1200px;
    height: 1200px;
    overflow: hidden;
    background: var(--stage-bg);
  }
  .stage {
    position: relative;
    width: 1200px;
    height: 1200px;
  }
  .book-cover {
    position: absolute;
    left: 297px;
    top: 96px;
    width: 601px;
    height: 962px;
    background: var(--cover-blue);
    color: var(--ink-white);
  }
  .title-block {
    position: absolute;
    left: 0;
    top: 0;
    width: 601px;
    height: 620px;
  }
  .title-block text {
    font-family: "Bebas Neue", "Oswald", sans-serif;
    fill: var(--ink-white);
  }
  .subtitle {
    position: absolute;
    left: 0;
    top: 628px;
    width: 601px;
    margin: 0;
    text-align: center;
    font-family: "Lato", sans-serif;
    font-weight: 400;
    font-size: 26px;
    line-height: 38px;
  }
  .subtitle strong { font-weight: 700; }
  .author-name {
    position: absolute;
    left: 75px;
    top: 870px;
    margin: 0;
    font-family: "Lato", sans-serif;
    font-weight: 700;
    font-size: 34px;
    line-height: 42px;
  }
  .publisher {
    position: absolute;
    left: 423px;
    top: 862px;
    display: flex;
    align-items: center;
    gap: 12px;
    font-family: "Lato", sans-serif;
  }
  .publisher-dot {
    width: 48px;
    height: 48px;
    border-radius: 50%;
    background: var(--ink-white);
  }
  .publisher-name {
    font-weight: 400;
    font-size: 17px;
    line-height: 17px;
    width: 80px;
  }
  .publisher-site {
    display: block;
    font-size: 14px;
    line-height: 17px;
  }
</style>
</head>
<body>
  <main class="stage">
    <section class="book-cover">
      <svg class="title-block" viewBox="0 0 601 620" aria-labelledby="cover-title">
        <title id="cover-title">The Steady Harbor Manual</title>
        <path d="M124 129 H91 V593 H521 V129 H190" fill="none" stroke="#ffffff" stroke-width="8"/>
        <text x="129" y="153" font-size="52" textLength="56" lengthAdjust="spacingAndGlyphs">THE</text>
        <text x="140" y="324" font-size="226" textLength="324" lengthAdjust="spacingAndGlyphs">STEADY</text>
        <text x="140" y="393" font-size="71" textLength="324" lengthAdjust="spacing">HARBOR</text>
        <text x="140" y="555" font-size="197" textLength="324" lengthAdjust="spacingAndGlyphs">MANUAL</text>
      </svg>

      <p class="subtitle">A <strong>practitioner's guide</strong><br>to building viable<br>products <strong>customers love</strong></p>

      <p class="author-name">Mira Solberg</p>

      <div class="publisher">
        <span class="publisher-dot"></span>
        <span class="publisher-name">Editora Verlindt<span class="publisher-site">verlindt.example</span></span>
      </div>
    </section>
  </main>
</body>
</html>
```